依頼詳細
配色は 水色・青系・その他 NGは白・ピンク系の色です

縦長 H1400xW600 の置き型看板(SYSTEM記載)
壁 H570xW850 店名ロゴのみ
記載項目
記載内容は
New Club Orva オルヴァ
SYSTEM 1set 50min
20:00~21:00 3.000
21:00~Last 5.000
延長 ハーフ 3.000
1time 5.000
TAX 20%
焼酎・ウイスキー 飲み放題
住所・TEL 〇〇〇
希望イメージ
シンプル 複雑
単色 カラフル
暗い 明るい
日常 高級
遊び心 厳粛
未来的 伝統的
女性的 男性的
希望する色
緑系、青系、水色系
納品ファイル
• 高解像度JPG (.jpg)
• イラストレーター形式 (.ai)
補足説明
■ 選んだ理由

店舗代表者が気に入りました

■ 提案者全員のお礼・コメント

この度は何度も変更等依頼しまして ご対応有難う御座いました

```html
<!DOCTYPE html>
<html lang="ja">
<head>
<meta charset="utf-8">
<title>New Club Orva – Stand Sign</title>
<link rel="stylesheet" href="https://fonts.googleapis.com/css2?family=Noto+Serif+JP:wght@500;700;900&display=swap">
<style>
  :root {
    --bg-top: #05070f;
    --bg-mid: #0b1430;
    --bg-bottom: #13285a;
    --text: #ffffff;
    --rule: #d8def0;
    --pill-start: #1c3f9e;
    --pill-mid: #2f63d0;
    --pill-end: #4fa3e6;
    --wing-deep: #0d2240;
    --wing-glow: #2e6f9a;
  }
  * { margin: 0; padding: 0; box-sizing: border-box; }
  html, body {
    width: 1200px;
    height: 3600px;
    overflow: hidden;
    background: var(--bg-top);
  }
  .sign {
    position: relative;
    width: 1200px;
    height: 3600px;
    overflow: hidden;
    font-family: "Noto Serif JP", "Times New Roman", serif;
    color: var(--text);
    background: linear-gradient(180deg, var(--bg-top) 0%, var(--bg-top) 30%, var(--bg-mid) 60%, var(--bg-bottom) 100%);
  }
  .butterfly-art {
    position: absolute;
    left: 0;
    top: 0;
    width: 1200px;
    height: 1340px;
    background:
      radial-gradient(ellipse 520px 600px at 760px 560px, rgba(46, 111, 154, 0.55), rgba(13, 34, 64, 0.35) 60%, transparent 100%),
      radial-gradient(ellipse 360px 300px at 900px 1100px, rgba(46, 111, 154, 0.35), transparent 100%);
  }
  .club-label {
    position: absolute;
    top: 1540px;
    width: 100%;
    text-align: center;
    font-size: 148px;
    font-weight: 700;
    line-height: 1;
    letter-spacing: 1px;
  }
  .club-name {
    position: absolute;
    top: 1800px;
    width: 100%;
    text-align: center;
    font-size: 290px;
    font-weight: 700;
    line-height: 1;
  }
  .system-heading {
    position: absolute;
    left: 128px;
    top: 2340px;
    display: flex;
    align-items: center;
    width: 952px;
    font-size: 88px;
    font-weight: 700;
    line-height: 1;
  }
  .system-heading::after {
    content: "";
    flex: 1;
    height: 4px;
    margin-left: 36px;
    background: var(--rule);
  }
  .set-pill {
    position: absolute;
    left: 120px;
    top: 2468px;
    width: 960px;
    height: 140px;
    border-radius: 70px;
    background: linear-gradient(90deg, var(--pill-start), var(--pill-mid) 55%, var(--pill-end));
    display: flex;
    align-items: center;
    justify-content: center;
    font-size: 84px;
    font-weight: 700;
  }
  .price-list {
    position: absolute;
    left: 128px;
    top: 2648px;
    width: 952px;
    list-style: none;
  }
  .price-row {
    display: flex;
    justify-content: space-between;
    align-items: center;
    height: 110px;
    font-size: 76px;
    font-weight: 700;
  }
  .tax-note {
    position: absolute;
    right: 120px;
    top: 3096px;
    font-size: 42px;
    font-weight: 700;
  }
  .footer-rule {
    position: absolute;
    left: 120px;
    top: 3200px;
    width: 960px;
    height: 4px;
    background: var(--rule);
  }
  .phone {
    position: absolute;
    left: 124px;
    top: 3262px;
    display: flex;
    align-items: center;
    font-size: 124px;
    font-weight: 700;
    line-height: 1;
    letter-spacing: 2px;
  }
  .phone svg { width: 124px; height: 124px; margin-right: 8px; }
  .address {
    position: absolute;
    left: 128px;
    top: 3440px;
    font-size: 44px;
    font-weight: 500;
  }
</style>
</head>
<body>
  <div class="sign">
    <div class="butterfly-art" role="img" aria-label="Translucent blue wireframe butterfly illustration"></div>

    <div class="club-label">New Club</div>
    <div class="club-name">Orva</div>

    <div class="system-heading">SYSTEM</div>
    <div class="set-pill">1set 50min</div>

    <ul class="price-list">
      <li class="price-row"><span>20:00~21:00</span><span>3,000</span></li>
      <li class="price-row"><span>21:00~Last</span><span>5,000</span></li>
      <li class="price-row"><span>延長・ハーフ</span><span>3,000</span></li>
      <li class="price-row"><span>1time</span><span>5,000</span></li>
    </ul>
    <div class="tax-note">TAX.20%</div>

    <div class="footer-rule"></div>

    <div class="phone">
      <svg viewBox="0 0 100 100" aria-hidden="true">
        <circle cx="50" cy="50" r="44" fill="none" stroke="#ffffff" stroke-width="8"/>
        <path d="M34 24c3-2 7-1 8 2l5 11c1 3 0 5-2 7l-4 3c3 7 8 12 15 15l3-4c2-2 4-3 7-2l11 5c3 1 4 5 2 8l-4 5c-3 3-8 4-13 2C46 71 31 56 26 40c-2-5-1-10 2-13z" fill="#ffffff"/>
      </svg>
      <span>123-456-7890</span>
    </div>
    <div class="address">〇〇件〇〇市〇〇町123456</div>
  </div>
</body>
</html>
```